Leading Nutrition Company Needs a Stylish Label Design!

We need a label/packaging design for our new cutting-edge detox called "Clear Tide". It is an all organic detox that removes toxins, harsh-chemicals, herbicides, pesticides and heavy metals from the body. It essentially turns everything you eat into organic whole foods and without all the chemicals in our bodies, we run at optimal performance.

We are attempting to blend a modern, simplistic design for our label.
We would like to see designs that use flat grays, silvers and blacks. We would also like to see pops of green and or blue in the design. Overall design will be a modern, contemporary matte finish with pops of color in either a pattern design or colored lettering. The final design should convey a high-end, exclusive health product.

Target Market(s)

Health conscious individuals and those seeking to pass an upcoming drug test. Athletes, nutritionist, dietitians ranging from 18-70 years of age.

Industry/Entity Type

Health

Font styles to use
Other font styles liked:
• Unique modern fonts

Colors
b1b1b1
9d9d9d
474747
33a6d7
0192cd
9ccb3b

Requirements
Must have
• Must be modern and simplistic

Pops of color - Don't need to be matte

Matte finishes for background
-Light grays, graphite, light silvers etc

Lettering must be modern and unique

Label type wil be a "shrink label" for an 8 oz boston squat bottle
-See attached link for bottle

"Clear Tide" some where on label

Company logo some where on label
-See attached files for logo
Nice to have
• Cool background designs that provide depth to the design.

A strip of pattern design running vertically or horizontally to capture the eye.
-See attached pictures for examples
Should not have
• Script or Normal fonts

```html
<!DOCTYPE html>
<html lang="en">
<head>
<meta charset="utf-8">
<title>Clear Tide Detox – 8 oz Label</title>
<link rel="stylesheet" href="https://fonts.googleapis.com/css2?family=Patua+One&family=Roboto:wght@700&display=swap">
<style>
  :root {
    --stage-grey: #c0c0c0;
    --label-white: #fbfbfc;
    --drop-blue: #13a5df;
    --tab-black: #111111;
    --ink-white: #ffffff;
    --ink-black: #1a1a1a;
  }
  html, body {
    margin: 0;
    padding: 0;
    width: 1200px;
    height: 748px;
    overflow: hidden;
    background: var(--stage-grey);
  }
  .canvas {
    position: relative;
    width: 1200px;
    height: 748px;
    background: var(--stage-grey);
  }
  .label {
    position: absolute;
    left: 231px;
    top: 247px;
    width: 737px;
    height: 313px;
    background: var(--label-white);
    overflow: hidden;
  }
  .label-pattern {
    position: absolute;
    inset: 0;
    background: linear-gradient(180deg, #fdfdfe 0%, #f4f4f7 100%);
  }
  .drop {
    position: absolute;
    left: 0;
    top: 0;
    width: 737px;
    height: 313px;
  }
  .brand-tab {
    position: absolute;
    left: 317px;
    top: 0;
    width: 85px;
    height: 117px;
    background: var(--tab-black);
    display: flex;
    flex-direction: column;
    align-items: center;
    justify-content: center;
    gap: 6px;
  }
  .brand-dot {
    width: 10px;
    height: 10px;
    border-radius: 50%;
    background: var(--ink-white);
  }
  .brand-name {
    font-family: "Patua One", serif;
    color: var(--ink-white);
    font-size: 15px;
    line-height: 1.05;
    text-align: center;
  }
  .product-name {
    position: absolute;
    left: 375px;
    top: 134px;
    transform: translateX(-50%);
    margin: 0;
    font-family: "Patua One", serif;
    font-weight: 400;
    font-size: 41px;
    line-height: 1;
    color: var(--ink-white);
    white-space: nowrap;
  }
  .product-type {
    position: absolute;
    left: 375px;
    top: 189px;
    transform: translateX(-50%);
    margin: 0;
    font-family: "Patua One", serif;
    font-size: 27px;
    line-height: 1;
    letter-spacing: 0.5px;
    color: var(--ink-white);
  }
  .volume {
    position: absolute;
    left: 357px;
    top: 288px;
    transform: translateX(-50%);
    margin: 0;
    font-family: "Roboto", sans-serif;
    font-weight: 700;
    font-size: 13px;
    color: var(--ink-black);
  }
</style>
</head>
<body>
  <main class="canvas">
    <section class="label" aria-label="Clear Tide Detox bottle label">
      <div class="label-pattern" role="img" aria-label="Soft grey dotted background pattern"></div>
      <svg class="drop" viewBox="0 0 737 313" aria-hidden="true">
        <path d="M288 292 C262 250 255 200 268 150 A112 112 0 1 1 400 262 C360 275 320 282 288 292 Z" fill="var(--drop-blue)"/>
      </svg>
      <div class="brand-tab">
        <span class="brand-dot"></span>
        <span class="brand-name">Vela<br>Nutri</span>
      </div>
      <h1 class="product-name">Clear Tide</h1>
      <p class="product-type">DETOX</p>
      <p class="volume">8 oz</p>
    </section>
  </main>
</body>
</html>
```